Website Design for Korvelin.com.au (Design + Code)

I am a small business specialising in aquarium monitoring solutions.
Our products essentially are computerised monitoring equipment for aquariums. E.g. https://www.tidalmetrix.example/en-GB/products-shop/vantora-units
and also GloWard http://www.gloward.example/
I see the design having 3 pages
* Landing / Home
* Gallery
* Contact us
Design:
I am looking for a cutting edge slick looking site. It should have a number of pages so the site is interactive with contact us, gallery etc.
I have attached our logo and can provide more info as requested. I will be constantly changing the site content as well from my end.
I have attached my logo design which was done via MakerPlume. It can be changed/altered if you feel something else would work better
Final deliverable:
* This project requires both design and development (coding).
* The 3 design pages are to be delivered as PSD files, and the coding as HTML.
The site will need to scale to be viewable on both oSlate/otabs etc as well as standard desktop
Hi All,
Just based on the couple of designs that have come through so far I would like to specify that for the front landing page, I don't want to be product specific, but rather a page that describes the company and some information about what we do and why it is important to monitor your aquarium. It would still be good to have some images of the monitoring equipment, I will provide or modify the text with the information I am talking about above.
I hope this a little more specific.
Hi All,
While I like the designs that are coming through, I still feel that they are all very template based in look and feel.
I am looking for a unique design that is interactive and engaging to the viewer.
If you need more information from me, please let me know.
Please feel free to submit completely new designs.
Kind Regards,
Tarvesh

```html
<!DOCTYPE html>
<html lang="en">
<head>
<meta charset="utf-8">
<title>Korvelin – Aquarium Monitoring Solutions</title>
<link href="https://fonts.googleapis.com/css2?family=Open+Sans:wght@400;600&family=Fjalla+One&display=swap" rel="stylesheet">
<style>
:root{
  --blue:#4aa3dc;
  --nav-active:#5a5a5a;
  --text:#8a8a8a;
  --heading:#4a4a4a;
  --line:#ececec;
  --panel:#f6f6f6;
  --footer:#050505;
  --white:#ffffff;
}
*{box-sizing:border-box;margin:0;padding:0}
html,body{width:1200px;height:1179px;overflow:hidden;background:var(--white);font-family:"Open Sans",sans-serif;color:var(--text)}
.page{position:relative;width:1200px;height:1179px}
.brand{position:absolute;left:171px;top:66px;display:flex;align-items:center;gap:10px}
.brand-mark{width:18px;height:18px;background:var(--blue)}
.brand-name{font-size:38px;font-weight:400;color:var(--heading);line-height:1}
.brand-tag{position:absolute;left:171px;top:113px;font-size:9.5px;color:var(--blue);letter-spacing:.2px}
.social{position:absolute;display:flex;gap:8px}
.social span{width:26px;height:26px;border-radius:50%;border:1px solid #d5d5d5;display:block}
.social.top{right:171px;top:41px}
.phone{position:absolute;right:171px;top:86px;font-size:16px;color:#8a8a8a;display:flex;align-items:center;gap:8px}
.nav{position:absolute;left:171px;top:141px;width:858px;height:49px;background:linear-gradient(#6bb8e6,#4ea3da);display:flex}
.nav a{color:var(--white);text-decoration:none;font-size:16px;line-height:49px;padding:0 28px;border-right:1px solid rgba(255,255,255,.18);text-shadow:0 1px 1px rgba(0,0,0,.25)}
.nav a.active{background:var(--nav-active);padding:0 16px;text-shadow:none}
.hero{position:absolute;left:171px;top:189px;width:858px;height:394px;background:radial-gradient(ellipse at 65% 45%,#e0a53a 0,#c88a2e 12%,#3fa0e0 30%,#2a86d0 70%,#1d6fb8 100%)}
.hero-title{position:absolute;left:212px;top:294px;font-family:"Fjalla One",sans-serif;font-weight:400;font-size:38px;line-height:46px;color:var(--white);white-space:nowrap}
.hero-text{position:absolute;left:212px;top:348px;width:316px;font-size:11px;line-height:20.5px;text-align:justify;color:var(--white)}
.dots{position:absolute;left:219px;top:433px;display:flex;gap:5px}
.dots span{width:11px;height:11px;border-radius:50%;background:#e6e6e6}
.dots span.on{background:#2f8a3a;border:2px solid #e6e6e6}
.quick{position:absolute;left:174px;top:604px;width:225px;height:431px;border:1px solid var(--line)}
.quick h2{background:var(--panel);height:51px;line-height:51px;padding-left:19px;font-weight:400;font-size:19px;color:var(--blue)}
.quick form{padding:18px 14px 0}
.quick label{display:block;font-size:11px;line-height:14px;color:#9a9a9a;margin:0 0 3px 2px}
.quick .field{height:34px;border:1px solid var(--line);margin-bottom:19px}
.quick .area{height:68px;margin-bottom:17px}
.quick .send{display:block;margin:0 auto;width:100px;height:33px;background:var(--blue);color:var(--white);border:0;border-radius:2px;font:400 11.5px "Open Sans",sans-serif}
.welcome{position:absolute;left:426px;top:601px;width:604px}
.welcome h2{font-weight:600;font-size:21.5px;color:var(--heading);margin-bottom:8px}
.welcome p{font-size:11px;line-height:20.5px;text-align:justify}
.more{display:block;color:var(--blue);font-size:12px;margin-top:8px;text-decoration:none}
.gallery-head{position:absolute;left:426px;top:760px;width:604px;display:flex;justify-content:space-between;align-items:center}
.gallery-head h2{font-weight:400;font-size:21px;color:#6a6a6a}
.arrows{display:flex;gap:8px}
.arrows span{width:18px;height:18px;border-radius:50%;border:1px solid #ccc;font-size:10px;line-height:16px;text-align:center;color:#555}
.cards{position:absolute;left:426px;top:804px;display:flex;gap:21px}
.card{width:187px;height:231px;border:1px solid var(--line);overflow:hidden}
.card .photo{height:138px}
.card h3{font-weight:400;font-size:14px;line-height:20px;color:#6a6a6a;margin:12px 12px 8px;white-space:nowrap}
.card p{font-size:11px;line-height:20px;margin:0 12px;text-align:justify}
.p1{background:linear-gradient(#2a7fb8,#3c8fa8 50%,#7a8a7a)}
.p2{background:linear-gradient(#1c4f8a,#3f7a60 55%,#5a8ab8)}
.p3{background:linear-gradient(#3a4a6a,#6a6a5a 55%,#4a5a4a)}
.footer{position:absolute;left:171px;top:1071px;width:858px;height:82px;background:var(--footer)}
.footer .brand-name{position:absolute;left:22px;top:30px;font-size:20px;color:#9a9a9a}
.footer .copy{position:absolute;left:168px;top:20px;font-size:12px;color:#a8a8a8}
.footer .links{position:absolute;left:168px;top:49px;font-size:11.5px;color:#a8a8a8;word-spacing:2px}
.social.bottom{right:27px;top:28px}
.social.bottom span{border-color:#555}
</style>
</head>
<body>
<div class="page">
  <header>
    <div class="brand"><span class="brand-mark"></span><span class="brand-name">Korvelin</span></div>
    <div class="brand-tag">AQUARIUM MONITORING SOLUTIONS</div>
    <div class="social top"><span></span><span></span><span></span></div>
    <div class="phone">
      <svg width="14" height="12" viewBox="0 0 14 12"><path d="M1 4c0-3 12-3 12 0v1H10V3.5H4V5H1z" fill="#1b5e96"/><rect x="3" y="6" width="8" height="5" rx="1" fill="#1b5e96"/></svg>
      Call : 08 9714 2268
    </div>
  </header>
  <nav class="nav">
    <a class="active" href="#">HOME</a><a href="#">About Us</a><a href="#">Products &amp; Services</a><a href="#">Gallery</a><a href="#">Solutions</a><a href="#">Contact Us</a>
  </nav>
  <div class="hero" role="img" aria-label="Banded butterflyfish swimming in blue water beside coral"></div>
  <h1 class="hero-title">Aquarium Monitoring</h1>
  <p class="hero-text">Lorem ipsum dolor sit amet, conse ctetur adipisicing elit, sed do eius mod tempor incididunt ut labore et dolore magna aliqua. Quisque bibendum eros</p>
  <div class="dots"><span class="on"></span><span></span><span></span><span></span></div>

  <aside class="quick">
    <h2>Quick Contact</h2>
    <form>
      <label>Name</label><div class="field"></div>
      <label>Phone No</label><div class="field"></div>
      <label>E Mail</label><div class="field"></div>
      <label>Your Enquiry...</label><div class="field area"></div>
      <button class="send" type="button">Send Enquiry</button>
    </form>
  </aside>

  <section class="welcome">
    <h2>Welcome To Korvelin</h2>
    <p>Lorem ipsum dolor sit amet, consectetur adipisc ng elit. Proin ultricies vestibulum velit, bibendum condimentum metus faucibus sed. Lorem ipsum dolor sit amet, consectetur adipisc ng elit. Proin ultricies vestibulum velit, bibendum condimentum metus faucibus sed. Lorem ipsum dolor sit amet, consectetur adipisc ng elit. Proin ultricies vestibulum velit, bibendum condimentum metus faucibus sed. Lorem ipsum dolor sit amet,</p>
    <a class="more" href="#">Read More</a>
  </section>

  <div class="gallery-head"><h2>Gallery</h2><div class="arrows"><span>&#8249;</span><span>&#8250;</span></div></div>
  <div class="cards">
    <div class="card"><div class="photo p1" role="img" aria-label="Reef aquarium with tropical fish"></div><h3>Sed ut perspiciatis unde</h3><p>Lorem ipsum dolor sit amet, eiusmod tempor incididunt</p></div>
    <div class="card"><div class="photo p2" role="img" aria-label="Planted aquarium with colourful fish"></div><h3>Sed ut perspiciatis unde</h3><p>Lorem ipsum dolor sit amet, eiusmod tempor incididunt</p></div>
    <div class="card"><div class="photo p3" role="img" aria-label="Rock aquascape with angelfish"></div><h3>Sed ut perspiciatis unde</h3><p>Lorem ipsum dolor sit amet, eiusmod tempor incididunt</p></div>
  </div>

  <footer class="footer">
    <span class="brand-name">Korvelin</span>
    <div class="copy">©2014 Korvelin , All Rights Reserved.</div>
    <div class="links">Home &nbsp;| &nbsp;About &nbsp;| &nbsp;About us &nbsp;&nbsp;| &nbsp;Solutions | &nbsp;Contact</div>
    <div class="social bottom"><span></span><span></span><span></span></div>
  </footer>
</div>
</body>
</html>
```